Informational Site for Advanced Chemistry R&D

The company develops oxidation chemistry for air, water, fuel pollution controls. The site has been prototyped at www.velmirlab.net. Take a look. Now, the task is to design it for eye-catching beauty with use of color, on-page scroll-driven color transition and parallax effects. Should capture the themes: high technology, wow it's beautiful, modern, uncluttered, clean urban environment.

Target Market(s)

China Environmentally Conscious Government and Industry,

Industry/Entity Type

It Company

Number of Pages Required

3 page

Font styles to use
Sans Serif

Requirements
Must have
• Parallax effects, desktop compatible, Rich, Modern, Simple, Graphic
Nice to have
• Mobile Phone Compatible
Should not have
• Flash, or anything that is slow to load or requires high bandwidth

```html
<!DOCTYPE html>
<html lang="en">
<head>
<meta charset="utf-8">
<title>Velmir Lab – Advanced Oxidation Science</title>
<link href="https://fonts.googleapis.com/css2?family=Oswald:wght@400;500&family=Open+Sans:wght@400;600;700&family=Raleway:wght@200&display=swap" rel="stylesheet">
<style>
:root{
  --teal:#2bb3b1;
  --ink:#222;
  --nav:#1f1f1f;
  --grey-bg:#f3f3f3;
  --text-grey:#666;
  --blue:#1b6fb5;
  --footer:#3a3637;
  --white:#fff;
}
*{margin:0;padding:0;box-sizing:border-box}
html,body{width:1200px;height:2381px;overflow:hidden}
body{position:relative;font-family:"Open Sans",Arial,sans-serif;color:var(--ink);background:var(--white)}
.abs{position:absolute}

/* header */
.top-line{left:0;top:0;width:1200px;height:5px;background:var(--teal)}
.brand{left:100px;top:38px;display:flex;align-items:center;gap:12px}
.brand-dot{width:30px;height:30px;border-radius:50%;background:var(--teal)}
.brand-name{font-weight:700;font-size:32px;color:var(--teal)}
.contact-top{top:38px;display:flex;align-items:center;gap:10px;font-size:14px;color:#444}
.contact-icon{width:30px;height:30px;border:2px solid var(--teal);border-radius:50%;display:flex;align-items:center;justify-content:center}
.nav-bar{left:0;top:100px;width:1200px;height:62px}
.nav{top:95px;left:776px;display:flex;height:67px;font-weight:700;font-size:12px}
.nav a{display:flex;align-items:center;padding:0 19px;color:#fff;text-decoration:none}
.nav a.active{background:var(--teal)}

/* hero */
.hero{left:0;top:162px;width:1200px;height:570px;overflow:hidden}
.hero-img{width:100%;height:100%;background:
  radial-gradient(ellipse 38% 30% at 50% 70%,#1f86b0 0%,#3aa6c8 40%,transparent 75%),
  radial-gradient(ellipse 70% 45% at 50% 80%,#6cc0d8 0%,#b9e1ec 55%,transparent 80%),
  linear-gradient(180deg,#fafdfe 0%,#e3f2f7 55%,#9fd3e3 82%,#5fb4cf 100%)}
.hero-caption{left:208px;top:290px;width:784px;height:181px;background:rgba(30,30,30,.82);display:flex;align-items:center;justify-content:center;text-align:center;font-family:"Raleway",sans-serif;font-weight:200;font-size:33px;line-height:62px;color:var(--teal);padding:0 20px}
.arrow{top:366px;width:32px;height:32px;border-radius:50%;background:rgba(120,170,200,.7);border:2px solid #fff;display:flex;align-items:center;justify-content:center}

/* about */
.about{left:0;top:730px;width:1200px;height:365px;background:var(--grey-bg)}
.h2{font-family:"Oswald",sans-serif;font-weight:500;color:var(--ink);text-align:center;width:1200px;left:0}
.about-text{left:152px;top:806px;width:896px;font-family:Arial,sans-serif;font-size:12px;line-height:23px;color:var(--text-grey);text-align:justify}
.solution{top:972px;width:120px;text-align:center;font-family:"Oswald",sans-serif;font-size:21px;color:var(--ink)}
.solution svg{display:block;margin:0 auto 10px}

/* advanced oxidation */
.adv{left:0;top:1095px;width:1200px;height:405px;background:
  radial-gradient(ellipse 25% 40% at 78% 30%,rgba(150,160,175,.5),transparent 70%),
  radial-gradient(ellipse 30% 35% at 30% 45%,rgba(110,120,135,.45),transparent 70%),
  linear-gradient(180deg,#1f2a3c 0%,#3e4756 45%,#555c66 65%,#2a303b 100%)}
.adv-text{left:98px;top:1130px;width:350px;color:#fff;font-family:Arial,sans-serif;font-size:12px;line-height:23px}
.adv-text h3{font-family:"Oswald",sans-serif;font-weight:500;font-size:25px;line-height:34px;margin-bottom:8px}
.adv-text ul{list-style:none;margin:10px 0}
.adv-text li{display:flex;align-items:center;gap:10px;font-size:13px;margin:6px 0}
.btn{display:inline-flex;align-items:center;gap:6px;margin-top:22px;background:#1d6fb8;color:#fff;font-family:"Oswald",sans-serif;font-size:13px;padding:8px 28px}
.screen-frame{left:620px;top:1158px;width:395px;height:264px;background:#151515;border-radius:12px;border:2px solid #8a8f95}
.screen{left:640px;top:1177px;width:355px;height:228px;background:#fff}
.screen-title{left:640px;top:1183px;width:355px;text-align:center;font-family:"Oswald",sans-serif;font-weight:500;font-size:12px;color:#333}
.screen-oh{left:692px;top:1208px;font-family:"Oswald",sans-serif;font-size:30px;color:var(--teal)}
.screen-text{left:653px;top:1262px;width:150px;font-family:Arial,sans-serif;font-size:8.5px;line-height:13px;color:#555;text-align:justify}
.screen-diagram{left:818px;top:1210px;width:168px;height:188px;background:radial-gradient(circle at 50% 50%,#e9f06a 0%,#f3f7b8 35%,#fff 70%)}
.laptop-base{left:555px;top:1420px;width:525px;height:14px;background:linear-gradient(180deg,#e8eaec,#a9aeb3);border-radius:0 0 14px 14px}

/* products */
.products{left:0;top:1500px;width:1200px;height:500px;background:var(--blue)}
.card{top:1595px;width:242px;height:368px;background:#1e1e1e;border:1px solid #111;overflow:hidden}
.card-img{width:100%;height:289px}
.card-label{height:79px;display:flex;flex-direction:column;align-items:center;justify-content:center;font-family:"Oswald",sans-serif;font-size:15px;line-height:26px;color:var(--teal);text-align:center}
.card-open{padding:30px 14px;color:#fff;background:linear-gradient(180deg,#2e2e2e,#121212)}
.card-open h4{font-family:"Oswald",sans-serif;font-weight:500;font-size:15px;line-height:26px;color:var(--teal);text-align:center;margin-bottom:10px}
.card-open p{font-family:Arial,sans-serif;font-size:12px;line-height:21px;text-align:justify}
.more{position:absolute;left:180px;top:318px;width:38px;height:38px;border-radius:50%;background:#fff;display:flex;align-items:center;justify-content:center;gap:3px}
.more i{width:5px;height:5px;border-radius:50%;background:var(--teal)}

/* partners & footer */
.partners{left:0;top:2000px;width:1200px;height:152px;background:var(--grey-bg)}
.footer{left:0;top:2152px;width:1200px;height:229px;background:var(--footer)}
.partner-band{left:98px;top:2073px;width:1002px;height:146px;background:linear-gradient(180deg,#1c1c1c,#333)}
.partner-badge{top:2104px;width:84px;height:84px;border-radius:50%}
.partner-name{top:2131px;left:226px;font-weight:700;font-size:18px;color:var(--teal)}
.footer-info{left:0;width:1200px;text-align:center;color:#fff;font-family:Arial,sans-serif;font-size:13px}
.social{top:2248px;left:566px;display:flex;gap:12px}
.social span{width:16px;height:16px;border-radius:50%;background:#fff}
.rule{left:186px;top:2338px;width:810px;height:1px;background:#888}
</style>
</head>
<body>
<div class="abs top-line"></div>

<div class="abs brand"><span class="brand-dot"></span><span class="brand-name">VelmirLab</span></div>

<div class="abs contact-top" style="left:785px"><span class="contact-icon"><svg width="12" height="9" viewBox="0 0 12 9"><rect width="12" height="9" fill="#333"/><path d="M0 0l6 5 6-5" stroke="#fff" fill="none"/></svg></span>info@velmirlab.net</div>
<div class="abs contact-top" style="left:965px"><span class="contact-icon"><svg width="8" height="13" viewBox="0 0 8 13"><rect x="0.5" y="0.5" width="7" height="12" rx="1" fill="none" stroke="#333"/><circle cx="4" cy="10.5" r=".8" fill="#333"/></svg></span>+1 555 014 2290</div>

<svg class="abs nav-bar" viewBox="0 0 1200 62" preserveAspectRatio="none"><polygon points="290,58 342,2 1200,2 1200,60 0,60 0,58" fill="var(--nav)"/></svg>
<nav class="abs nav"><a class="active">HOME</a><a>TECHNOLOGY</a><a>PRODUCTS ▾</a><a>CONTACT</a></nav>

<section class="abs hero">
  <div class="hero-img" role="img" aria-label="Close-up photograph of a water splash with droplets"></div>
</section>
<div class="abs hero-caption">Advanced Oxidation Science for Environmental Pollution Management</div>
<div class="abs arrow" style="left:26px"><svg width="14" height="12" viewBox="0 0 14 12"><path d="M13 6H2M6 1L1 6l5 5" stroke="#fff" stroke-width="2" fill="none"/></svg></div>
<div class="abs arrow" style="left:1142px"><svg width="14" height="12" viewBox="0 0 14 12"><path d="M1 6h11M8 1l5 5-5 5" stroke="#fff" stroke-width="2" fill="none"/></svg></div>
<svg class="abs" style="left:0;top:640px" width="1200" height="95" viewBox="0 0 1200 95"><path d="M0 55 C300 0 700 10 1200 85 L1200 95 L0 95Z" fill="var(--teal)"/><path d="M0 72 C300 20 700 30 1200 95 L0 95Z" fill="var(--grey-bg)"/></svg>

<section class="abs about"></section>
<h2 class="abs h2" style="top:756px;font-size:26px">About Velmir Lab</h2>
<p class="abs about-text">Velmir Lab develops advanced oxidation technologies and materials, which it licenses to Orvane Systems, China. Orvane Systems is engaged in the sales, service and support of environmental solutions for industry and government. With offices in Shanghai, Beijing, Shijiazhuang, and Chengdu, Orvane Systems is among the most advanced and rapidly growing companies offering solutions for air, water and fuel environmental compliance. Velmir Lab Corporation supports these solutions with research and development. Velmir Lab Corporation pursues business development opportunities in markets worldwide.</p>
<h3 class="abs h2" style="top:914px;font-size:22px">Solutions</h3>
<div class="abs solution" style="left:418px"><svg width="34" height="48" viewBox="0 0 34 48"><path d="M17 2 C24 16 32 24 32 32 A15 15 0 0 1 2 32 C2 24 10 16 17 2Z" fill="var(--teal)"/><path d="M9 32 a8 8 0 0 0 6 8" stroke="#fff" stroke-width="2" fill="none"/></svg>Water</div>
<div class="abs solution" style="left:540px"><svg width="44" height="48" viewBox="0 0 44 48"><g stroke="var(--teal)" stroke-width="2.5" fill="none" stroke-linecap="round"><path d="M4 16h26a6 6 0 1 0-6-6"/><path d="M4 24h34a5 5 0 1 1-5 5"/><path d="M4 32h18a5 5 0 1 1-5 5"/></g></svg>Air</div>
<div class="abs solution" style="left:664px"><svg width="44" height="48" viewBox="0 0 44 48"><rect x="6" y="4" width="22" height="40" rx="2" fill="var(--teal)"/><rect x="10" y="9" width="14" height="10" fill="#fff"/><path d="M28 14l8 6v18a3 3 0 0 1-6 0v-10h-2" stroke="var(--teal)" stroke-width="2.5" fill="none"/></svg>FUEL</div>

<section class="abs adv" role="img" aria-label="Blurred city skyline at dusk"></section>
<div class="abs adv-text">
  <h3>Advanced Oxidation</h3>
  <p>Advanced Oxidation refers to a variety of techniques employing the Hydroxyl Radical, an energetic, highly reactive cousin of the water molecule :</p>
  <ul>
    <li><svg width="10" height="13" viewBox="0 0 10 13"><path d="M5 0C7 4 10 6 10 8A5 5 0 0 1 0 8C0 6 3 4 5 0Z" fill="var(--teal)"/></svg>To add oxygen to inorganic molecules</li>
    <li><svg width="10" height="13" viewBox="0 0 10 13"><path d="M5 0C7 4 10 6 10 8A5 5 0 0 1 0 8C0 6 3 4 5 0Z" fill="var(--teal)"/></svg>To remove hydrogen from organic molecules</li>
  </ul>
  <p>These transformations convert important industrial contaminants into reactive forms that can be captured or that disintegrate into harmless end products.</p>
  <span class="btn">READ MORE ➜</span>
</div>
<div class="abs screen-frame"></div>
<div class="abs screen"></div>
<div class="abs screen-title">Chemical Reactions in the Atmosphere</div>
<div class="abs screen-oh">•OH</div>
<p class="abs screen-text">The Hydroxyl Radical is electrically neutral and as a result, the Oxygen atom has an unpaired valence electron (Signified here with the dot). This makes it highly reactive, wanting to steal an electron from any nearby molecule to form the Hydroxyl Ion, a common component of water.</p>
<div class="abs screen-diagram" role="img" aria-label="Reaction diagram of the hydroxyl radical linking to atmospheric molecules"></div>
<div class="abs laptop-base"></div>

<section class="abs products"></section>
<h2 class="abs h2" style="top:1533px;font-size:26px;color:#1d2733">Our Products</h2>
<div class="abs card card-open" style="left:98px">
  <h4>FLUE GAS SCRUBBING<br>FGVX</h4>
  <p>Coal-fired boilers produce smog as flue gas components react in the atmosphere. Sulfur emissions in the form of sulfuric acid cause acid rain and acid particulates. When they react with air born ammonia, from agricultural fertilizer and atmospheric nitrogen, they form ammonium sulfate haze. Nitrogen emissions in the form of nitric acids and peroxides.</p>
  <span class="more"><i></i><i></i><i></i></span>
</div>
<div class="abs card" style="left:352px"><div class="card-img" role="img" aria-label="Wastewater flowing from a drain pipe into a stream" style="background:linear-gradient(180deg,#3f5a2c 0%,#6b7a3e 30%,#9a8450 55%,#b8a77e 75%,#8f8a72 100%)"></div><div class="card-label">WASTEWATER TREATMENT<br>PEVX</div></div>
<div class="abs card" style="left:606px"><div class="card-img" role="img" aria-label="Black and white refinery towers" style="background:radial-gradient(ellipse 40% 60% at 50% 60%,#777,transparent 70%),linear-gradient(180deg,#8a8a8a 0%,#4a4a4a 45%,#262626 100%)"></div><div class="card-label">FUEL OIL DESULFURIZATION<br>PDVX</div></div>
<div class="abs card" style="left:861px"><div class="card-img" role="img" aria-label="Worker handling blue chemical drums" style="background:radial-gradient(ellipse 50% 40% at 60% 80%,#2a6bb0,transparent 75%),linear-gradient(180deg,#5f7a8e 0%,#3c5d80 45%,#1f4f8a 100%)"></div><div class="card-label">VOLATILE ORGANIC COMPOUNDS<br>VCVX</div></div>

<section class="abs partners"></section>
<section class="abs footer"></section>
<h2 class="abs h2" style="top:2021px;font-size:26px">Our Partners</h2>
<div class="abs partner-band"></div>
<span class="abs partner-name">Orvane Systems</span>
<span class="abs partner-badge" style="left:458px;background:#c6333c"></span>
<span class="abs partner-badge" style="left:658px;background:#1c5a9a"></span>
<span class="abs partner-badge" style="left:868px;background:#b01a22"></span>

<div class="abs social"><span></span><span></span><span></span></div>
<p class="abs footer-info" style="top:2275px"><svg width="8" height="11" viewBox="0 0 8 11"><path d="M4 11C1 7 0 5 0 4a4 4 0 0 1 8 0c0 1-1 3-4 7Z" fill="#fff"/></svg> Velmir Lab Corporation, Brookvale, New Jersey, U.S.A.</p>
<p class="abs footer-info" style="top:2299px">✉ info@velmirlab.net &nbsp;&nbsp;&nbsp; ▯ +1 555 014 2290</p>
<div class="abs rule"></div>
<p class="abs footer-info" style="top:2352px;font-size:12px">Copyright 2016 velmirlab. All rights reserved. <span style="color:var(--teal)">☝ Back to top</span></p>
</body>
</html>
```